Velmar Industrial Coatings

We are looking to improve our business cards. Our company installs industrial floor and wall coatings in industrial, chemical and food processing plants.
Our coatings which consist of epoxy, urethane, and vinyl esters provide chemical and abrasion resistant surface with non-skid properties that are easy to clean.

Target Market(s)

food manufacturing, chemical plants, breweries and wineries, warehouses, clean room floors.

Industry/Entity Type

Construction

Contact Information for Business Card

improved current logo.

Colors

Designer to choose colors to be used in the design.

Requirements
Must have
• the information from uploaded file
Nice to have
• "We'll be outstanding on your floors."

```html
<!DOCTYPE html>
<html lang="en">
<head>
<meta charset="utf-8">
<title>Colin Marsh – Velmar Industrial Coatings</title>
<link rel="stylesheet" href="https://fonts.googleapis.com/css2?family=Jost:wght@600;700;800&display=swap">
<style>
  :root {
    --accent-red: #f2310f;
    --ink: #111111;
    --panel-top: #f3f3f5;
    --panel-mid: #dcdde0;
    --panel-bottom: #a9abaf;
    --photo-wall: #c9cde8;
    --photo-floor: #5f86d6;
    --photo-deep: #3c5fb0;
  }
  * { margin: 0; padding: 0; box-sizing: border-box; }
  html, body { width: 1200px; height: 720px; overflow: hidden; background: #ffffff; }
  .business-card {
    position: relative;
    width: 1200px;
    height: 720px;
    overflow: hidden;
    font-family: "Jost", "Futura", sans-serif;
    color: var(--ink);
  }
  .info-panel {
    position: absolute;
    left: 0; top: 0;
    width: 600px; height: 720px;
    background: linear-gradient(180deg, var(--panel-top) 0%, var(--panel-mid) 55%, var(--panel-bottom) 100%);
  }
  .job-photo {
    position: absolute;
    left: 606px; top: 0;
    width: 594px; height: 720px;
    background:
      linear-gradient(180deg, var(--photo-wall) 0%, #d7daf0 38%, #8fa7e0 55%, var(--photo-floor) 75%, var(--photo-deep) 100%);
  }
  .accent-bars {
    position: absolute;
    left: 590px; top: 0;
    width: 30px; height: 720px;
  }
  .contact-name {
    position: absolute;
    left: 0; top: 98px;
    width: 640px;
    text-align: center;
    font-weight: 800;
    font-size: 56px;
    letter-spacing: 0.5px;
    color: var(--accent-red);
    line-height: 1;
  }
  .toll-free {
    position: absolute;
    left: 0; top: 172px;
    width: 640px;
    text-align: center;
    font-weight: 700;
    font-size: 32px;
    letter-spacing: 1px;
    line-height: 1;
  }
  .contact-group {
    position: absolute;
    font-weight: 700;
    font-size: 28px;
    line-height: 33px;
    text-transform: uppercase;
  }
  .contact-group.phones { left: 181px; top: 278px; }
  .contact-group.address { left: 186px; top: 422px; }
  .contact-group.online { left: 183px; top: 555px; }
  .contact-icon {
    position: absolute;
    width: 40px; height: 40px;
  }
  .contact-icon.phone { left: 98px; top: 306px; }
  .contact-icon.pin { left: 100px; top: 430px; }
  .contact-icon.globe { left: 100px; top: 566px; }
</style>
</head>
<body>
  <div class="business-card">
    <div class="info-panel">
      <div class="contact-name">COLIN MARSH</div>
      <div class="toll-free">1-800-555-0147</div>

      <svg class="contact-icon phone" viewBox="0 0 24 24" aria-hidden="true">
        <path fill="var(--ink)" d="M6.6 2.5l3 3.2-1.9 2.4c1.2 2.6 3.3 4.9 6.1 6.3l2.4-1.9 3.3 3-1.6 3.4c-.4.8-1.3 1.2-2.2 1-7.2-1.8-12.1-7.6-13.6-13.9-.2-.9.3-1.8 1.1-2.2z"/>
      </svg>
      <div class="contact-group phones">
        <div>Office: (360) 555-0131</div>
        <div>Fax: (360) 555-0133</div>
        <div>Cell: (360) 555-0176</div>
      </div>

      <svg class="contact-icon pin" viewBox="0 0 24 24" aria-hidden="true">
        <path fill="var(--ink)" d="M12 1.5c-4 0-7 3-7 6.8 0 4.6 7 11.2 7 11.2s7-6.6 7-11.2c0-3.8-3-6.8-7-6.8zm0 4.2a2.7 2.7 0 110 5.4 2.7 2.7 0 010-5.4z"/>
        <rect x="6" y="21" width="12" height="1.8" fill="var(--ink)"/>
      </svg>
      <div class="contact-group address">
        <div>P.O.Box 42</div>
        <div>Alder Creek, WA 98500</div>
      </div>

      <svg class="contact-icon globe" viewBox="0 0 24 24" aria-hidden="true">
        <circle cx="12" cy="12" r="10.5" fill="var(--ink)"/>
        <g fill="none" stroke="var(--panel-bottom)" stroke-width="1.2">
          <ellipse cx="12" cy="12" rx="4.5" ry="10.5"/>
          <line x1="12" y1="1.5" x2="12" y2="22.5"/>
          <line x1="1.5" y1="12" x2="22.5" y2="12"/>
          <path d="M3.5 6.5h17M3.5 17.5h17"/>
        </g>
      </svg>
      <div class="contact-group online">
        <div>colin@velmarfloors.com</div>
        <div>www.velmarfloors.com</div>
      </div>
    </div>

    <div class="job-photo" role="img" aria-label="Photo of a worker spreading a glossy blue epoxy coating across a warehouse floor with a squeegee"></div>

    <svg class="accent-bars" viewBox="0 0 30 720" preserveAspectRatio="none" aria-hidden="true">
      <polygon points="4,0 26,0 26,176 4,196" fill="var(--accent-red)"/>
      <polygon points="4,550 26,530 26,720 4,720" fill="var(--accent-red)"/>
    </svg>
  </div>
</body>
</html>
```